Poster needed for hilariously funny interactive FARCE!!

Buried Under the Blender is a hilarious interactive murder mystery that takes place in a coffeehouse and bookstore called “Bistro Marmalade.” The crazy cast of characters leads the audience through a maze of funny twists and turns. Opportunities for audience and cast interaction reach a peak when the audience is allowed to vote on the ending that they want to hear! There are four possible killers and four possible endings!
Updates

Hello Designers, I am trying to get PIXELHIVE to extend the time of this project. Thanks for your patience. RTP

Target Market(s)

Community and professional Theatres as well as amateur theatre groups

Industry/Entity Type

Cafe

Requirements
Must have
• It must have the title and credit.
• BURIED UNDER THE BLENDER by Rob Tapley
• 'Hilariously funny interactive Murder Mystery'
Nice to have
• The show deals with a coffee shop called 'Bistro Marmalade' and murder! It is a farce so it should relay that message through the poster.
Should not have
• Photos or images from movies..

```html
<!DOCTYPE html>
<html lang="en">
<head>
<meta charset="utf-8">
<title>Buried Under the Blender — Poster</title>
<link rel="stylesheet" href="https://fonts.googleapis.com/css2?family=Alfa+Slab+One&family=Bangers&family=Oswald:wght@600;700&display=swap">
<style>
  :root {
    --frame-red: #d9141b;
    --frame-dark: #8e0a0e;
    --wall-black: #161312;
    --wall-brown: #3a2a22;
    --title-red: #e3202a;
    --banner-yellow: #ffd11a;
    --banner-orange: #f6a313;
    --tag-red: #d81f26;
    --copy-white: #ffffff;
    --venue-gold: #f7b416;
    --smoke: rgba(220, 220, 220, 0.45);
  }
  * { margin: 0; padding: 0; box-sizing: border-box; }
  html, body { width: 927px; height: 1200px; overflow: hidden; background: var(--wall-black); }
  .poster {
    position: relative;
    width: 927px; height: 1200px;
    overflow: hidden;
    background: var(--frame-red);
  }
  .brick-wall {
    position: absolute;
    inset: 24px;
    background:
      radial-gradient(ellipse at 85% 4%, rgba(190, 90, 40, 0.55), transparent 30%),
      radial-gradient(ellipse at 50% 45%, var(--wall-brown), var(--wall-black) 70%);
    box-shadow: inset 0 0 40px 10px var(--frame-dark);
  }
  .smoke { position: absolute; width: 240px; height: 300px; top: 760px; }
  .smoke--left { left: 24px; background: radial-gradient(ellipse at 20% 50%, var(--smoke), transparent 65%); }
  .smoke--right { right: 24px; background: radial-gradient(ellipse at 80% 50%, var(--smoke), transparent 65%); }

  .title-block {
    position: absolute; left: 0; top: 150px; width: 927px;
    text-align: center;
    font-family: "Alfa Slab One", serif;
    font-weight: 400;
    color: var(--title-red);
    line-height: 1;
  }
  .title-line { display: block; }
  .title-line--buried { font-size: 160px; }
  .title-line--under { font-size: 96px; margin-top: 24px; }
  .title-line--blender { font-size: 138px; margin-top: 24px; }
  .credit {
    position: absolute; left: 0; top: 720px; width: 927px;
    text-align: center;
    font-family: "Oswald", sans-serif; font-weight: 700;
    font-size: 32px; line-height: 1; letter-spacing: 4px;
    color: var(--copy-white);
  }

  .tagline-band {
    position: absolute; left: 160px; top: 866px;
    width: 607px; height: 112px;
    background: linear-gradient(180deg, var(--banner-yellow), var(--banner-orange));
    clip-path: polygon(2% 6%, 98% 0, 100% 60%, 95% 100%, 5% 97%, 0 45%);
  }
  .tagline {
    position: absolute; left: 0; width: 927px; text-align: center;
    color: var(--tag-red); line-height: 1;
  }
  .tagline--main {
    top: 874px;
    font-family: "Bangers", sans-serif;
    font-size: 62px; letter-spacing: 2px;
  }
  .tagline--sub {
    top: 938px;
    font-family: "Oswald", sans-serif; font-weight: 600;
    font-size: 30px;
  }
  .blurb {
    position: absolute; left: 0; top: 1004px; width: 927px;
    text-align: center;
    font-family: "Oswald", sans-serif; font-weight: 600;
    font-size: 36px; line-height: 50px;
    color: var(--copy-white);
  }
  .blurb__venue { color: var(--venue-gold); }
</style>
</head>
<body>
<div class="poster">
  <div class="brick-wall" role="img" aria-label="Dark scorched brick wall texture with glowing ember light in the top right"></div>
  <div class="smoke smoke--left" role="img" aria-label="Wisps of grey smoke"></div>
  <div class="smoke smoke--right" role="img" aria-label="Wisps of grey smoke"></div>

  <h1 class="title-block">
    <span class="title-line title-line--buried">BURIED</span>
    <span class="title-line title-line--under">UNDER THE</span>
    <span class="title-line title-line--blender">BLENDER</span>
  </h1>
  <p class="credit">BY ROB TAPLEY</p>

  <div class="tagline-band"></div>
  <p class="tagline tagline--main">HILARIOUSLY FUNNY</p>
  <p class="tagline tagline--sub">INTERACTIVE MURDER MYSTERY</p>

  <p class="blurb">The show deals with a coffee shop called<br><span class="blurb__venue">'Bistro Marmalade'</span> and murder!</p>
</div>
</body>
</html>
```